movie poster for a bittersweet romantic drama

Hello everyone. Looking for a dynamic poster for feature film 'Maple's Lantern' a romantic drama. It is a bittersweet love story so not rosey lovie dovie type.

300dpi

Please visit the link below for the poster image
https://www.filecrate.example/s/k7x2p41hrq9zt5m/_R8K4417.tif?dl=0

poster should have:
1. title of film : Maple's Lantern
2. tagline of film:
Death knows no names
Love does not know race

3. A film by Harriet B. Okonkwe
4 Include the logo for 'Tolubi Pictures' attached below

poster size:
1. 8x10
2. thumnail
3. landscape with just film title
4. 27 by 41

Target Market(s)

15-55 men and mostly women

Industry/Entity Type

Film Production

Colors

Designer to choose colors to be used in the design.

Requirements
Must have
• Dynamic and vibrant
• it is a romantic drama so love on a serious note
Nice to have
• Play with romantic fonts but don't overdo it.
Should not have
• must not look like a romance novel

```html
<!DOCTYPE html>
<html lang="en">
<head>
<meta charset="utf-8">
<title>Maple's Lantern — Poster</title>
<link rel="stylesheet" href="https://fonts.googleapis.com/css2?family=Bodoni+Moda:opsz,wght@6..96,400&family=Jost:wght@300;600;700&display=swap">
<style>
  :root {
    --sky: #7eb9ea;
    --sky-light: #a9d2f3;
    --white: #ffffff;
    --ink: #1d2a4a;
    --field-green: #3d9a3a;
    --field-yellow: #d9dc2a;
    --field-orange: #d9895a;
    --field-teal: #4f7f72;
    --field-olive: #5f6e2c;
  }
  * { margin: 0; padding: 0; box-sizing: border-box; }
  html, body { width: 960px; height: 1200px; overflow: hidden; background: var(--sky); }
  .poster {
    position: relative;
    width: 960px;
    height: 1200px;
    background: linear-gradient(90deg, var(--sky) 0%, var(--sky-light) 20%, var(--sky) 50%, var(--sky-light) 80%, var(--sky) 100%);
    overflow: hidden;
  }
  .landscape-strip {
    position: absolute;
    left: 188px;
    top: 0;
    width: 560px;
    height: 1200px;
    background: linear-gradient(90deg,
      var(--field-teal) 0%,
      var(--field-teal) 10%,
      var(--field-orange) 18%,
      var(--field-yellow) 26%,
      var(--field-green) 34%,
      var(--field-olive) 44%,
      var(--field-olive) 56%,
      var(--field-green) 66%,
      var(--field-yellow) 74%,
      var(--field-orange) 82%,
      var(--field-teal) 90%,
      var(--field-teal) 100%);
  }
  .poster-type {
    position: absolute;
    inset: 0;
  }
  .title { font-family: 'Bodoni Moda', 'Didot', serif; font-weight: 400; fill: var(--white); }
  .credit { font-family: 'Jost', 'Futura', sans-serif; font-weight: 600; fill: var(--white); letter-spacing: 1px; }
  .tagline { font-family: 'Jost', 'Futura', sans-serif; font-weight: 300; fill: var(--white); }
  .tagline .strong { font-weight: 700; }
  .studio-mark {
    position: absolute;
    left: 756px;
    top: 996px;
    width: 134px;
    height: 120px;
    background: var(--white);
    display: flex;
    align-items: center;
    justify-content: center;
    text-align: center;
    font-family: 'Jost', 'Futura', sans-serif;
    font-weight: 600;
    font-size: 19px;
    line-height: 1.15;
    color: var(--ink);
    text-transform: uppercase;
  }
</style>
</head>
<body>
<main class="poster">
  <div class="landscape-strip" role="img" aria-label="Mirrored aerial photograph of green, yellow and orange flowering fields stretching vertically"></div>

  <svg class="poster-type" width="960" height="1200" viewBox="0 0 960 1200">
    <text class="title" x="120" y="584" font-size="170" textLength="688" lengthAdjust="spacingAndGlyphs">MAPLE’S</text>
    <text class="title" x="128" y="720" font-size="170" textLength="672" lengthAdjust="spacingAndGlyphs">LANTERN</text>
    <text class="credit" x="414" y="744" font-size="19" textLength="356" lengthAdjust="spacingAndGlyphs">A FILM BY HARRIET B. OKONKWE</text>
    <text class="tagline" x="54" y="1177" font-size="34" textLength="838" lengthAdjust="spacingAndGlyphs"><tspan class="strong">DEATH</tspan> KNOWS NO NAMES  <tspan class="strong">LOVE</tspan> DOES NOT KNOW RACE</text>
  </svg>

  <div class="studio-mark">Tolubi<br>Pictures</div>
</main>
</body>
</html>
```